St. Bramwell School
St. Bramwell School Fernvale
i have upload design please check it
I would appreciate your feedback on my designs.
Regards
PrimoPixelWorks4
Designers: I have uploaded the logo and pictures to be used in the brochure. The project details are in the brief. Once the design is set, I will work with the designer to add text.
The logo has been uploaded.
where we can find the details of this project...can you upload the details in pdf format or in word format..so that we can start designing it.
tandemvisuals
Philippines

```html
<!DOCTYPE html>
<html lang="en">
<head>
<meta charset="utf-8">
<title>St. Bramwell School Brochure</title>
<link rel="stylesheet" href="https://fonts.googleapis.com/css2?family=Open+Sans:wght@400;600;700;800&display=swap">
<style>
:root{
  --backdrop:#d4862f;
  --page-top:#eef5fb;
  --page-bottom:#c9ddef;
  --navy:#1d4689;
  --navy-dark:#143466;
  --red:#c4202d;
  --ink:#2b3345;
  --frame:#ffffff;
  --photo-warm-a:#b7a48a;
  --photo-warm-b:#6f5a48;
  --photo-cool-a:#a8c2d8;
  --photo-cool-b:#5f7f9c;
  --photo-green-a:#8fb36b;
  --photo-green-b:#4d7a3c;
  --map-a:#e4e6e2;
  --map-b:#b9c3c9;
}
*{box-sizing:border-box;margin:0;padding:0}
html,body{width:1200px;height:420px;overflow:hidden}
body{background:var(--backdrop);font-family:"Open Sans",Arial,sans-serif;color:var(--ink);position:relative}
.page{position:absolute;top:22px;height:376px;background:linear-gradient(180deg,var(--page-top),var(--page-bottom));box-shadow:0 3px 8px rgba(0,0,0,.35)}
.cover{left:20px;width:320px;overflow:hidden}
.spread{left:352px;width:480px;display:flex}
.back{left:844px;width:336px;padding:10px 12px}
.photo{position:absolute;border:3px solid var(--frame);box-shadow:0 1px 3px rgba(0,0,0,.3)}
.photo.warm{background:linear-gradient(135deg,var(--photo-warm-a),var(--photo-warm-b))}
.cover .building{left:14px;top:14px;width:236px;height:104px;background:linear-gradient(180deg,#f5f2ec,#d7cbb9)}
.cover .tagline{position:absolute;left:18px;top:122px;font-size:7px;color:var(--navy)}
.cover .wave{position:absolute;left:0;top:0;width:320px;height:376px}
.school-name-block{position:absolute;left:30px;top:168px;font-weight:700;font-size:20px;line-height:1.1;color:var(--navy);width:150px}
.cover .students{left:0;top:268px;width:150px;height:108px;border:none;box-shadow:none}
.column{position:relative;width:240px;height:100%;padding:8px 9px}
.column + .column{border-left:1px solid rgba(29,70,137,.2)}
.bar{background:linear-gradient(180deg,var(--navy),var(--navy-dark));color:#fff;font-weight:700;font-size:8.5px;padding:3px 6px;border-radius:2px;margin-bottom:4px}
.body{font-size:5.6px;line-height:1.45;margin-bottom:5px}
.list{list-style:none;font-size:5.6px;line-height:1.55}
.list li::before{content:"\2022";color:var(--red);margin-right:3px}
.row{display:flex;gap:6px;margin-bottom:6px}
.box{position:relative;border:3px solid var(--frame);box-shadow:0 1px 3px rgba(0,0,0,.3)}
.caption{font-size:5px;font-weight:600;color:var(--navy);margin:2px 0 5px}
.map-row{display:flex;gap:8px;margin:4px 0 8px}
.map{width:210px;height:118px;background:linear-gradient(135deg,var(--map-a),var(--map-b));border:1px solid #9aa}
.legend{list-style:none;font-size:6px;line-height:1.7;padding-top:24px}
.legend li::before{content:"";display:inline-block;width:8px;height:1px;background:var(--ink);margin-right:3px;vertical-align:middle}
.address{display:flex;justify-content:space-between;align-items:center;border-top:2px solid var(--navy);padding-top:8px;font-size:6px;line-height:1.55}
.address .school-name{font-weight:700;color:var(--navy)}
.back-name{font-weight:700;font-size:9px;color:var(--navy);width:64px;line-height:1.15;margin-right:8px}
</style>
</head>
<body>

<section class="page cover">
  <svg class="wave" viewBox="0 0 320 376" aria-hidden="true">
    <path d="M0 250 C90 225 200 270 320 235 L320 376 L0 376 Z" fill="#d4e4f3"/>
    <path d="M150 376 C175 320 250 300 320 300 L320 376 Z" fill="#b6cfe6"/>
  </svg>
  <div class="photo building" role="img" aria-label="Photo of the school building exterior"></div>
  <p class="tagline">St. Bramwell School Fernvale</p>
  <p class="school-name-block">St. Bramwell School</p>
  <div class="photo warm students" role="img" aria-label="Photo of students working together at a desk"></div>
</section>

<section class="page spread">
  <div class="column">
    <h2 class="bar">Mission Statement</h2>
    <p class="body">We nurture every child in faith, learning and service, guiding each student to grow in mind, heart and spirit within a caring Catholic community that values respect, kindness and excellence.</p>
    <div class="row">
      <ul class="list">
        <li>Full day kindergarten</li>
        <li>Small class sizes</li>
        <li>Music and art programs</li>
        <li>Before and after care</li>
        <li>Faith formation daily</li>
      </ul>
      <div>
        <div class="box" style="width:100px;height:60px;background:linear-gradient(135deg,var(--photo-cool-a),var(--photo-warm-b))" role="img" aria-label="Photo of a teacher with students in a classroom"></div>
        <p class="caption">Our Classroom</p>
      </div>
    </div>
    <h2 class="bar">Sign Ups</h2>
    <div class="row">
      <p class="body" style="width:110px">Enrollment for the new school year is open. Visit the school office or call us to arrange a tour and meet our teachers.</p>
      <div class="box" style="width:100px;height:56px;background:linear-gradient(135deg,var(--photo-cool-a),var(--photo-cool-b))" role="img" aria-label="Photo of children at computers"></div>
    </div>
    <div class="box" style="width:110px;height:66px;background:linear-gradient(135deg,var(--photo-warm-a),var(--photo-warm-b))" role="img" aria-label="Photo of students in the school library"></div>
  </div>
  <div class="column">
    <h2 class="bar">School Philosophy</h2>
    <p class="body">At St. Bramwell School we believe every student learns best when faith, family and school work together in a safe and joyful setting.</p>
    <h2 class="bar">Extended Facility</h2>
    <div class="row">
      <p class="body" style="width:110px">Our campus offers a library, computer lab, gym and outdoor play fields, with supervised care from early morning until evening.</p>
      <div class="box" style="width:100px;height:62px;background:linear-gradient(135deg,var(--photo-cool-a),var(--photo-warm-b))" role="img" aria-label="Photo of the school gym"></div>
    </div>
    <div class="row">
      <div>
        <div class="box" style="width:120px;height:82px;background:linear-gradient(160deg,var(--photo-green-a),var(--photo-green-b))" role="img" aria-label="Photo of a child playing soccer outdoors"></div>
        <p class="caption">Outdoor Play</p>
      </div>
      <div class="box" style="width:88px;height:60px;background:linear-gradient(135deg,var(--photo-warm-a),var(--photo-cool-b))" role="img" aria-label="Photo of children at a school event"></div>
    </div>
    <h2 class="bar">Outreach and Activities</h2>
    <ul class="list">
      <li>Sports teams and clubs</li>
      <li>Parish service projects</li>
      <li>Student council</li>
      <li>Science fair</li>
    </ul>
  </div>
</section>

<section class="page back">
  <h2 class="bar">Spiritual Growth and Christian Values</h2>
  <ul class="list" style="margin-bottom:8px">
    <li>Weekly Mass with families</li>
    <li>Daily prayer and reflection</li>
    <li>Service learning in each grade</li>
    <li>Sacrament preparation programs</li>
    <li>Retreats for older students</li>
  </ul>
  <h2 class="bar">Locate Us At</h2>
  <div class="map-row">
    <div class="map" role="img" aria-label="Area map showing the school location"></div>
    <ul class="legend">
      <li>Fernvale</li>
      <li>Hillcrest</li>
      <li>Lakeview</li>
      <li>Brookside</li>
      <li>Elmwood</li>
    </ul>
  </div>
  <div class="address">
    <div>
      <p class="school-name">St. Bramwell School</p>
      <p>2480 Linden Avenue</p>
      <p>Fernvale, WI 53999</p>
      <p>Phone: 555-014-2266</p>
      <p>Fax: 555-014-2267</p>
      <p>office@stbramwell.example</p>
    </div>
    <p class="back-name">St. Bramwell School</p>
  </div>
</section>

</body>
</html>
```